【 概要 】 自社メディアに誘導する広告バナーとサムネイルデザインを募集します。 【 依頼内容 】 ・サイズ: 横 × 縦1200×628 ・作成数: 1種類×1サイズ ★サムネイル用は参考画像があります。 ・利用用途:バナー広告 【 デザインイメージ 】 ・参考デザイン:検索エンジンに引っかからないようにするため、コメントにて記載Googleドキュメントのテキストにて添付いたします。 こちらより参考にしてくださいませ。 https://docs.kumorinote.jp/document/d/7Qw3LrT9zXbN2mKpVcYhS8dFgJ4uE6oiAa1Bc5Wx_Rz/edit?usp=sharing 【 契約金額(税抜) 】 2,000円 ※契約金額(税込)からシステム利用料を差し引いた金額が、ワーカーさまの受取金額となります その他ご質問等ありましたら、気軽にお問い合わせください。 ご応募をお待ちしております! |
| https://kurashimori.tanemaki-hub.jp/localblog/nami_poolclub.html | ||
どの案も素敵だったのですが、こちらのデザインで決めさせていただきました。
みなさまありがとうございました。

```html
<!DOCTYPE html>
<html lang="ja">
<head>
<meta charset="UTF-8">
<title>オトナの停滞肌をレスキュー!</title>
<link href="https://fonts.googleapis.com/css2?family=Noto+Sans+JP:wght@500;700;900&family=M+PLUS+Rounded+1c:wght@700;800&display=swap" rel="stylesheet">
<style>
  :root {
    --pink-light: #fde8f0;
    --pink-mid: #f8c6d9;
    --pink-deep: #f1a3c2;
    --gold: #c9a25a;
    --ink: #2b2b2b;
    --rescue-red: #e23049;
    --bubble-gray: #6b6b6b;
    --white: #ffffff;
    --ribbon-tail: #c98aa0;
  }
  html, body {
    margin: 0;
    padding: 0;
    overflow: hidden;
    background: var(--white);
  }
  .banner {
    position: relative;
    width: 1200px;
    height: 628px;
    overflow: hidden;
    font-family: "Noto Sans JP", sans-serif;
    color: var(--ink);
    background:
      radial-gradient(circle at 78% 22%, rgba(255,255,255,.85) 0 40px, transparent 120px),
      radial-gradient(circle at 15% 85%, rgba(255,255,255,.6) 0 30px, transparent 140px),
      radial-gradient(circle at 50% 50%, var(--pink-light) 0, var(--pink-mid) 65%, var(--pink-deep) 100%);
  }
  .photo {
    position: absolute;
    overflow: hidden;
  }
  .photo--consultation {
    left: -30px; top: -20px;
    width: 290px; height: 290px;
    border-radius: 50%;
    background: linear-gradient(135deg, #f3ece8 0%, #d9c9c2 50%, #3a2d2d 100%);
    border: 6px solid var(--white);
  }
  .photo--products {
    left: -40px; top: 300px;
    width: 340px; height: 340px;
    border-radius: 50%;
    background: radial-gradient(circle at 45% 45%, #ffffff 0, #e9eef3 45%, #9fb2d6 80%, #2f3f9a 100%);
  }
  .photo--advisor {
    right: 0; top: 40px;
    width: 290px; height: 588px;
    background: linear-gradient(180deg, rgba(255,255,255,0) 0%, #e7d6d2 18%, #3a2e2e 42%, #141414 100%);
    border-radius: 140px 0 0 0;
  }
  .frame {
    position: absolute;
    left: 0; top: 0;
  }
  .dots {
    position: absolute;
    top: 112px; left: 384px;
    display: flex;
    gap: 26px;
  }
  .dots span {
    width: 14px; height: 14px;
    border-radius: 50%;
    background: var(--rescue-red);
  }
  .age {
    position: absolute;
    left: 366px; top: 132px;
    font-family: "M PLUS Rounded 1c", sans-serif;
    font-weight: 800;
    font-size: 70px;
    line-height: 1;
    letter-spacing: -1px;
  }
  .age small {
    font-size: 48px;
    margin-left: 2px;
  }
  .age-from {
    position: absolute;
    left: 535px; top: 180px;
    font-weight: 700;
    font-size: 26px;
  }
  .concern {
    position: absolute;
    display: flex;
    align-items: center;
    justify-content: center;
    width: 88px; height: 88px;
    border-radius: 50%;
    background: var(--bubble-gray);
    color: var(--white);
    font-weight: 700;
    font-size: 26px;
  }
  .concern--dry { left: 620px; top: 56px; }
  .concern--sag { left: 650px; top: 128px; }
  .concern--dull { left: 744px; top: 92px; }
  .headline {
    position: absolute;
    left: 310px; width: 600px;
    top: 258px;
    text-align: center;
    font-weight: 900;
    font-size: 52px;
    line-height: 1;
  }
  .headline .particle { font-size: 38px; }
  .rescue {
    position: absolute;
    left: 310px; width: 600px;
    top: 332px;
    text-align: center;
    font-weight: 900;
    font-size: 92px;
    line-height: 1;
    color: var(--rescue-red);
    letter-spacing: 2px;
  }
  .ribbon {
    position: absolute;
    left: 0; top: 0;
  }
  .ribbon-text {
    position: absolute;
    left: 246px; width: 628px;
    top: 486px; height: 58px;
    display: flex;
    align-items: center;
    justify-content: center;
    font-weight: 700;
    font-size: 24px;
  }
  .ribbon-text strong {
    font-weight: 900;
    font-size: 33px;
  }
</style>
</head>
<body>
  <div class="banner">
    <div class="photo photo--consultation" role="img" aria-label="美容部員が女性客の肌をカウンセリングしている写真"></div>
    <div class="photo photo--products" role="img" aria-label="白いボトルと青い美容液ボトルが水しぶきと並ぶ商品写真"></div>
    <div class="photo photo--advisor" role="img" aria-label="黒い服に赤いスカーフの美容アドバイザーが手で案内している写真"></div>

    <svg class="frame" width="1200" height="628" viewBox="0 0 1200 628" aria-hidden="true">
      <path d="M334,44 H886 A24,24 0 0 0 910,68 V432 A24,24 0 0 0 886,456 H334 A24,24 0 0 0 310,432 V68 A24,24 0 0 0 334,44 Z"
            fill="#ffffff" stroke="var(--gold)" stroke-width="5"/>
      <path d="M344,54 H876 A22,22 0 0 0 900,78 V422 A22,22 0 0 0 876,446 H344 A22,22 0 0 0 320,422 V78 A22,22 0 0 0 344,54 Z"
            fill="none" stroke="var(--gold)" stroke-width="2"/>
    </svg>

    <div class="dots"><span></span><span></span><span></span></div>
    <div class="age">30<small>代</small></div>
    <div class="age-from">からの</div>
    <div class="concern concern--dry">乾燥</div>
    <div class="concern concern--sag">たるみ</div>
    <div class="concern concern--dull">くすみ</div>

    <div class="headline">オトナ<span class="particle">の</span>停滞肌<span class="particle">を</span></div>
    <div class="rescue">レスキュー!</div>

    <svg class="ribbon" width="1200" height="628" viewBox="0 0 1200 628" aria-hidden="true">
      <polygon points="214,500 262,500 262,560 214,560 228,530" fill="var(--ribbon-tail)"/>
      <polygon points="986,500 938,500 938,560 986,560 972,530" fill="var(--ribbon-tail)" transform="translate(-80,0)"/>
      <polygon points="246,544 262,560 262,544" fill="#7d4a5a"/>
      <polygon points="874,544 858,560 858,544" fill="#7d4a5a"/>
      <rect x="246" y="484" width="628" height="60" fill="#ffffff" stroke="var(--ink)" stroke-width="3"/>
    </svg>
    <div class="ribbon-text"><strong>ハナミズキ化粧品</strong>さんに聞いてみた!</div>
  </div>
</body>
</html>
```